5 page simple power point for Crest of Morning Stables

All content provided for 4 slides of a power point presentation. I would like the first slide to be very bold with a large image (one that I've provided) to get the audience attention. You don't have to use all the images, just the ones that fit best. Please use the attached Crest of Morning logo on all slides. Be as creative as you want, this will be on tv. Here is the content for the slides:

Slide 1

Crest of Morning Stables
A National, Next Generation Thoroughbred Horse Racing Syndication
with an "inside the ropes experience"

Racing in New York, Maryland, California, West Virginia, Pennsylvania, Kentucky and Florida

20 horses in our stable
Over 150 co-owners - 75% are new owners
Winning percentage - 27%, in the money - 64%

Slide 2 - Why not thoroughbred ownership?

1. Financial Commitment too big - afraid of ongoing expenses

2. Don't know enough about it, perhaps a little intimidating

Slide 3

The Crest of Morning Difference

Small Financial Commitment -
*Shares are $2,000
*Gain ownership in 2-3 horses
*In over 80 quarters, we've had 6 distributions and 4 capital calls
*Quarterly financial reports for all groups

Slide 4 Owner Education

*The Fenceline Digest and the Gallop
*Barn Chatter
*Complete Transparency - when it happens, our co-owners know about it
*Co-owner get togethers at Linden Vale and Brookhurst
*We don't want you to BE an owner, we want you to BECOME an owner

Slide 5

The "HOLLOWAY EXPERIENCE"
*First of it's kind. Holloway is the test market
*Partner with Tom and Greta Vansworth & Helen Ashgrove & Owen Pike
*Purchase 2-3 thoroughbreds to train at Vansworth Stables
*Provide a farm to starting gate experience - connection with horses
*Receptions at the farm - watch workouts, ferrier, meet with trainer, etc.
*HAVE FUN and ENJOY being an owner

Target Market(s)

men/women 40+

Requirements
Must have
• Simple and easy to read yet eye catching
Nice to have
• easy to read but something that pops
Should not have
• nothing cartoonlike or whimsical

```html
<!DOCTYPE html>
<html lang="en">
<head>
<meta charset="utf-8">
<title>Crest of Morning Stables – Presentation Slides</title>
<link rel="stylesheet" href="https://fonts.googleapis.com/css2?family=Cinzel:wght@400;600;700&family=Arimo:ital,wght@0,400;0,700;1,400&family=Questrial&family=Oswald:wght@500&display=swap">
<style>
  :root{
    --gold:#c0962f;
    --gold-soft:rgba(196,160,70,.9);
    --navy:#2c2f7c;
    --navy-deep:#24276b;
    --list:#4a4f9c;
    --paper:#ffffff;
    --shadow:#6e6e6e;
  }
  *{box-sizing:border-box;margin:0;padding:0}
  html,body{width:720px;height:1200px;overflow:hidden;background:var(--paper)}
  .board{position:relative;width:720px;height:1200px;overflow:hidden;background:var(--paper);font-family:"Questrial",sans-serif;color:var(--navy)}
  .board__wedge{position:absolute;inset:0}

  .slide{position:absolute;width:320px;height:180px;background:var(--paper);overflow:hidden;box-shadow:3px 3px 0 var(--shadow)}

  .brand-mark{position:absolute;display:flex;align-items:center}
  .brand-mark__dot{width:11px;height:11px;border-radius:50%;background:var(--gold)}

  .photo{position:absolute}

  /* Hero */
  .hero{position:absolute;left:107px;top:33px;width:505px;height:299px;background:#141414;padding:7px;box-shadow:3px 3px 0 var(--shadow)}
  .hero__photo{position:relative;width:100%;height:100%;overflow:hidden;
    background:
      radial-gradient(ellipse 48% 30% at 70% 22%, rgba(58,70,150,.75), rgba(58,70,150,0) 70%),
      radial-gradient(ellipse 55% 45% at 55% 58%, rgba(52,28,16,.95), rgba(52,28,16,0) 75%),
      radial-gradient(ellipse 30% 22% at 30% 45%, rgba(30,20,12,.8), rgba(30,20,12,0) 75%),
      linear-gradient(180deg,#3f5a2c 0%,#6c7a4a 18%,#c7c1ab 30%,#7d6a4f 48%,#8e7758 75%,#c9b592 100%)}
  .hero__shade{position:absolute;inset:0;background:linear-gradient(180deg,rgba(0,0,0,.1),rgba(0,0,0,.45) 50%,rgba(0,0,0,.15))}
  .hero__text{position:absolute;left:0;right:0;top:137px;text-align:center;color:#fff;font-family:"Cinzel",serif}
  .hero__title{font-size:26px;font-weight:600;letter-spacing:2px;line-height:1}
  .hero__sub{font-size:14px;font-weight:600;letter-spacing:2.5px;margin-top:8px}
  .hero__tag{font-family:"Questrial",sans-serif;font-size:8px;letter-spacing:2.4px;margin-top:12px}

  /* Stats slides */
  .stats__head{position:absolute;left:0;right:0;top:10px;text-align:center}
  .stats__title{font-family:"Cinzel",serif;font-weight:600;font-size:12px;letter-spacing:4px;color:var(--navy-deep);line-height:1}
  .stats__stables{font-family:"Arimo",sans-serif;font-weight:700;font-size:7px;letter-spacing:2.6px;margin-top:2px;color:var(--navy-deep)}
  .stats__line{font-size:5.8px;color:var(--navy);line-height:1.35}
  .stats__line b{font-family:"Arimo",sans-serif}
  .stats__grid{position:absolute;top:52px;left:24px;width:274px;height:115px}
  .tile{position:absolute;color:#fff;font-family:"Arimo",sans-serif;font-size:5.6px;line-height:1.25;overflow:hidden}
  .tile--a{left:0;top:0;width:87px;height:115px}
  .tile--b{left:93px;top:0;width:87px;height:47px}
  .tile--c{left:93px;top:53px;width:87px;height:62px}
  .tile--d{left:187px;top:0;width:87px;height:115px}
  .tile__cap{position:absolute;left:4px;right:4px;text-shadow:0 0 2px rgba(0,0,0,.7)}
  .num{font-family:"Oswald",sans-serif;font-style:italic;font-size:12px;margin-right:2px}
  .sepia .tile--a{background:radial-gradient(ellipse 60% 45% at 60% 40%,#4a3820,rgba(74,56,32,0) 75%),linear-gradient(180deg,#b99c68,#e7cf98 60%,#a48858)}
  .sepia .tile--b{background:radial-gradient(ellipse 35% 55% at 40% 40%,#5c4626,rgba(92,70,38,0) 75%),linear-gradient(180deg,#e4c98c,#bfa46e)}
  .sepia .tile--c{background:radial-gradient(ellipse 70% 40% at 50% 70%,#3e2f1b,rgba(62,47,27,0) 80%),linear-gradient(180deg,#6b5636,#4a3a24)}
  .sepia .tile--d{background:radial-gradient(ellipse 40% 25% at 50% 38%,#3e301c,rgba(62,48,28,0) 80%),linear-gradient(180deg,#f3dca0,#d9bf86 55%,#a38955)}
  .cool .tile--a{background:radial-gradient(ellipse 60% 45% at 60% 40%,#2e3050,rgba(46,48,80,0) 75%),linear-gradient(180deg,#8d90b4,#c9cbe2 60%,#7c7fa6)}
  .cool .tile--b{background:radial-gradient(ellipse 35% 55% at 40% 40%,#3c3e66,rgba(60,62,102,0) 75%),linear-gradient(180deg,#b8badb,#8a8db4)}
  .cool .tile--c{background:radial-gradient(ellipse 70% 40% at 50% 70%,#25274a,rgba(37,39,74,0) 80%),linear-gradient(180deg,#4e5180,#33355c)}
  .cool .tile--d{background:radial-gradient(ellipse 40% 25% at 50% 38%,#262848,rgba(38,40,72,0) 80%),linear-gradient(180deg,#c3c5e0,#a1a4c8 55%,#7a7da6)}

  /* Content slides */
  .heading{font-family:"Arimo",sans-serif;font-weight:700;color:var(--navy);font-size:12px;line-height:1.25}
  .list{list-style:none;font-family:"Questrial",sans-serif;font-size:6px;line-height:1.3;color:var(--navy)}
  .list li{position:relative;padding-left:12px;margin-bottom:2.6px}
  .list li::before{content:"";position:absolute;left:2px;top:1.6px;width:4px;height:4px;background:var(--navy);clip-path:polygon(0 0,100% 50%,0 100%)}

  .why__copy{position:absolute;left:21px;top:46px;width:150px}
  .why__item{font-family:"Arimo",sans-serif;font-weight:700;font-size:7.6px;margin-top:9px}
  .why__note{font-size:5.8px;margin-top:1px}

  .diff__copy{position:absolute;left:159px;top:47px;width:155px}
  .diff__copy .list{margin-top:6px}

  .edu__panel{position:absolute;left:216px;top:0;width:104px;height:180px;background:var(--navy)}
  .edu__box{position:absolute;left:172px;top:27px;width:126px;height:136px;background:var(--gold-soft);padding:12px 8px 0 9px}
  .edu__box .heading{font-family:"Questrial",sans-serif;font-weight:400;font-size:11.5px;color:var(--navy)}
  .edu__box .list{margin-top:7px;color:var(--list)}

  .hollow__copy{position:absolute;left:173px;top:26px;width:138px}
  .hollow__title{font-family:"Arimo",sans-serif;font-weight:700;font-size:11px;letter-spacing:3px;line-height:1.35;color:var(--navy)}
  .hollow__copy .list{margin-top:8px}

  /* Checklist */
  .checklist{position:absolute;left:78px;top:993px;list-style:none;font-family:"Arimo",sans-serif;font-size:16px;color:var(--navy);line-height:21.3px}
  .checklist li{display:flex;align-items:center;gap:10px}
  .checklist__box{width:14px;height:14px;border:2.5px solid var(--navy);box-shadow:2px 2px 0 var(--navy);flex:none}
  .checklist__sub{padding-left:32px}
  .checklist__sub .checklist__sq{width:7px;height:7px;background:var(--navy);flex:none;margin-top:-4px}
</style>
</head>
<body>
<main class="board">
  <svg class="board__wedge" width="720" height="1200" viewBox="0 0 720 1200" aria-hidden="true">
    <polygon points="0,5 720,1200 0,1200" fill="var(--gold)"/>
  </svg>

  <!-- Opening slide -->
  <section class="hero">
    <div class="hero__photo" role="img" aria-label="Jockey in blue and yellow silks riding a bay racing thoroughbred at full gallop past the rail">
      <div class="hero__shade"></div>
      <div class="hero__text">
        <div class="hero__title">CREST OF MORNING</div>
        <div class="hero__sub">STABLES</div>
        <div class="hero__tag">NEXT GENERATION OWNERSHIP</div>
      </div>
    </div>
  </section>

  <!-- Stats slide, warm version -->
  <section class="slide stats sepia" style="left:30px;top:372px">
    <div class="brand-mark" style="right:14px;top:6px"><span class="brand-mark__dot"></span></div>
    <header class="stats__head">
      <div class="stats__title">CREST OF MORNING</div>
      <div class="stats__stables">STABLES</div>
      <div class="stats__line">A National, Next Generation Thoroughbred Horse Racing Syndication<br>with an <b>"inside the ropes experience"</b></div>
    </header>
    <div class="stats__grid">
      <div class="tile tile--a" role="img" aria-label="Jockey racing a thoroughbred down the track">
        <div class="tile__cap" style="bottom:12px;text-align:center"><b><i>RACING</i></b> in New York, Maryland, California, West Virginia, Pennsylvania, Kentucky and Florida</div>
      </div>
      <div class="tile tile--b" role="img" aria-label="Horse looking out from a stable stall">
        <div class="tile__cap" style="bottom:5px"><span class="num">20</span>Horses in our stables</div>
      </div>
      <div class="tile tile--c" role="img" aria-label="Group of co-owners standing together">
        <div class="tile__cap" style="top:16px"><span class="num">150</span><i>Co-owners</i></div>
        <div class="tile__cap" style="bottom:6px"><span class="num">75 %</span>Are New owners</div>
      </div>
      <div class="tile tile--d" role="img" aria-label="Rider jumping a horse over a fence">
        <div class="tile__cap" style="bottom:31px"><span class="num">27 %</span>Winning</div>
        <div class="tile__cap" style="bottom:11px"><span class="num">64%</span>in the money</div>
      </div>
    </div>
  </section>

  <!-- Stats slide, cool version -->
  <section class="slide stats cool" style="left:370px;top:403px">
    <div class="brand-mark" style="right:14px;top:6px"><span class="brand-mark__dot"></span></div>
    <header class="stats__head">
      <div class="stats__title">CREST OF MORNING</div>
      <div class="stats__stables">STABLES</div>
      <div class="stats__line">A National, Next Generation Thoroughbred Horse Racing Syndication<br>with an <b>"inside the ropes experience"</b></div>
    </header>
    <div class="stats__grid">
      <div class="tile tile--a" role="img" aria-label="Jockey racing a thoroughbred down the track">
        <div class="tile__cap" style="bottom:12px;text-align:center"><b><i>RACING</i></b> in New York, Maryland, California, West Virginia, Pennsylvania, Kentucky and Florida</div>
      </div>
      <div class="tile tile--b" role="img" aria-label="Horse looking out from a stable stall">
        <div class="tile__cap" style="bottom:5px"><span class="num">20</span>Horses in our stables</div>
      </div>
      <div class="tile tile--c" role="img" aria-label="Group of co-owners standing together">
        <div class="tile__cap" style="top:16px"><span class="num">150</span><i>Co-owners</i></div>
        <div class="tile__cap" style="bottom:6px"><span class="num">75 %</span>Are New owners</div>
      </div>
      <div class="tile tile--d" role="img" aria-label="Rider jumping a horse over a fence">
        <div class="tile__cap" style="bottom:31px"><span class="num">27 %</span>Winning</div>
        <div class="tile__cap" style="bottom:11px"><span class="num">64%</span>in the money</div>
      </div>
    </div>
  </section>

  <!-- Why not ownership -->
  <section class="slide why" style="left:30px;top:581px">
    <svg class="photo" width="320" height="180" viewBox="0 0 320 180" role="img" aria-label="Woman gently stroking a chestnut horse wearing a red halter">
      <defs>
        <linearGradient id="whyTone" x1="0" y1="0" x2="1" y2="0">
          <stop offset="0" stop-color="#8a3f1e"/><stop offset=".38" stop-color="#b8602f"/>
          <stop offset=".6" stop-color="#d9b27a"/><stop offset=".82" stop-color="#e6d7b4"/><stop offset="1" stop-color="#c6a25e"/>
        </linearGradient>
        <radialGradient id="whyGlow" cx=".85" cy=".1" r=".5"><stop offset="0" stop-color="#f4eedb" stop-opacity=".8"/><stop offset="1" stop-color="#f4eedb" stop-opacity="0"/></radialGradient>
      </defs>
      <polygon points="195,0 320,0 320,180 148,180" fill="url(#whyTone)"/>
      <polygon points="195,0 320,0 320,180 148,180" fill="url(#whyGlow)"/>
    </svg>
    <div class="brand-mark" style="left:9px;top:7px"><span class="brand-mark__dot"></span></div>
    <div class="why__copy">
      <h2 class="heading">Why not thoroughbred ownership?</h2>
      <div class="why__item">1. Financial Commitment</div>
      <div class="why__note">too big - afraid of ongoing expenses</div>
      <div class="why__item" style="margin-top:4px">2. Don't know enough</div>
      <div class="why__note">about it, perhaps a little intimidating</div>
    </div>
  </section>

  <!-- The difference -->
  <section class="slide diff" style="left:371px;top:617px">
    <svg class="photo" width="320" height="180" viewBox="0 0 320 180" role="img" aria-label="Jockey in red silks winning a race on a bay thoroughbred">
      <defs>
        <linearGradient id="diffTone" x1="0" y1="0" x2="0" y2="1">
          <stop offset="0" stop-color="#8a8886"/><stop offset=".25" stop-color="#b23a2e"/>
          <stop offset=".45" stop-color="#5a3220"/><stop offset=".7" stop-color="#2f3a5a"/>
          <stop offset=".82" stop-color="#9a9a94"/><stop offset="1" stop-color="#4f8a3a"/>
        </linearGradient>
      </defs>
      <polygon points="0,0 162,0 126,180 0,180" fill="url(#diffTone)"/>
    </svg>
    <div class="brand-mark" style="right:14px;top:7px"><span class="brand-mark__dot"></span></div>
    <div class="diff__copy">
      <h2 class="heading">The CREST OF MORNING difference</h2>
      <ul class="list">
        <li>Small Financial Commitment</li>
        <li>Shares are $2,000</li>
        <li>Gain ownership in 2-3 horses</li>
        <li>In over 80 quarters, we've had 6 distributions and 4 capital calls</li>
        <li>Quarterly financial reports for all groups</li>
      </ul>
    </div>
  </section>

  <!-- Owner education -->
  <section class="slide edu" style="left:30px;top:801px">
    <div class="photo" style="left:0;top:0;width:216px;height:180px;background:radial-gradient(ellipse 40% 60% at 30% 60%,#241a16,rgba(36,26,22,0) 80%),linear-gradient(100deg,#d8c7a6 0%,#a08a6a 22%,#3a2a22 45%,#c99a7a 62%,#2f56a0 80%,#2a3f86 100%)" role="img" aria-label="Trainer holding the halter of a dark horse"></div>
    <div class="edu__panel"></div>
    <div class="brand-mark" style="left:9px;top:7px"><span class="brand-mark__dot"></span></div>
    <div class="edu__box">
      <h2 class="heading">Owner Education</h2>
      <ul class="list">
        <li>The Fenceline Digest and the Gallop</li>
        <li>Barn Chatter</li>
        <li>Complete Transparency - when it happens, our co-owners know about it</li>
        <li>Co-owner get togethers at Linden Vale and Brookhurst</li>
        <li>We don't want you to <i>BE</i> an owner, we want you to <i>BECOME</i> an owner</li>
      </ul>
    </div>
  </section>

  <!-- Holloway experience -->
  <section class="slide hollow" style="left:371px;top:834px">
    <div class="photo" style="left:0;top:0;width:80px;height:87px;background:linear-gradient(180deg,#6f7a6a 0%,#a6a49a 35%,#3a3a40 65%,#4f7a36 100%)" role="img" aria-label="Owners gathered for a group photo at the farm"></div>
    <div class="photo" style="left:84px;top:0;width:80px;height:87px;background:linear-gradient(180deg,#2f4a22 0%,#4a5a3a 35%,#6f9a3f 65%,#8ab44a 100%)" role="img" aria-label="Foals running in a green paddock"></div>
    <div class="photo" style="left:0;top:91px;width:80px;height:89px;background:linear-gradient(160deg,#5a6a4a 0%,#9a5a32 40%,#3e2a1e 70%,#8a4a3a 100%)" role="img" aria-label="Two horses at a paddock fence"></div>
    <div class="photo" style="left:84px;top:91px;width:80px;height:89px;background:linear-gradient(180deg,#c8ccd0 0%,#6f8a5a 40%,#4a3a30 60%,#a8a29a 100%)" role="img" aria-label="Rider jumping a horse in an arena"></div>
    <div class="brand-mark" style="right:14px;top:7px"><span class="brand-mark__dot"></span></div>
    <div class="hollow__copy">
      <h2 class="hollow__title">The "Holloway Experience"</h2>
      <ul class="list">
        <li>First of it's kind. Holloway is the test market</li>
        <li>Partner with Tom and Greta Vansworth &amp; Helen Ashgrove &amp; Owen Pike</li>
        <li>Purchase 2-3 thoroughbreds to train at Vansworth Stables</li>
        <li>Provide a farm to starting gate experience - connection with horses</li>
        <li>Receptions at the farm - watch workouts, ferrier, meet with trainer, etc.</li>
        <li><i>HAVE FUN</i> and <i>ENJOY</i> being an owner</li>
      </ul>
    </div>
  </section>

  <!-- Feature checklist -->
  <ul class="checklist">
    <li><span class="checklist__box"></span>Ratio 16:9</li>
    <li><span class="checklist__box"></span>Full HD</li>
    <li><span class="checklist__box"></span>Custom color pallet Gold and Blue as COM logo</li>
    <li><span class="checklist__box"></span>Custom Font -&nbsp; Easy Change</li>
    <li class="checklist__sub"><span class="checklist__sq"></span>Halden Sans</li>
    <li class="checklist__sub"><span class="checklist__sq"></span>Corvale Gothic</li>
    <li><span class="checklist__box"></span>Easy to edit, just drag and drop images</li>
    <li><span class="checklist__box"></span>Can be included more slides</li>
    <li><span class="checklist__box"></span>In the sample include two opening for Slide -1</li>
  </ul>
</main>
</body>
</html>
```